Vantrell Law Letterhead

We need a new letterhead design for a Law Firm. The address for the law firm is 4817 Larkspur Boulevard, Suite 250, Houston, Texas 77342. Phone Number: 832-619-3057; Fax Number: 832-407-1694. The logo is uploaded to the project.

```html
<!DOCTYPE html>
<html lang="en">
<head>
<meta charset="utf-8">
<title>Vantrell Law Letterhead</title>
<link rel="stylesheet" href="https://fonts.googleapis.com/css2?family=Open+Sans:wght@400;600&display=swap">
<style>
  :root {
    --navy: #1f3264;
    --red: #e21d25;
    --ink: #3a3a3a;
    --backdrop: #eeeff1;
    --paper: #ffffff;
    --faint-navy: #d3d8e3;
  }
  * { margin: 0; padding: 0; box-sizing: border-box; }
  html, body {
    width: 1200px; height: 840px; overflow: hidden;
    background: var(--backdrop);
    font-family: "Open Sans", sans-serif;
  }
  .letterhead {
    position: absolute; left: 320px; top: 28px;
    width: 560px; height: 784px;
    background: var(--paper);
    box-shadow: 0 2px 10px rgba(0,0,0,0.12);
    overflow: hidden;
  }
  .band-top-navy { position: absolute; top: 0; left: 0; right: 0; height: 8px; background: var(--navy); }
  .band-top-red { position: absolute; top: 12px; left: 0; right: 0; height: 18px; background: var(--red); }
  .band-bottom-red { position: absolute; bottom: 16px; left: 0; right: 0; height: 18px; background: var(--red); }
  .band-bottom-navy { position: absolute; bottom: 0; left: 0; right: 0; height: 12px; background: var(--navy); }

  .brand {
    position: absolute; left: 50px; top: 98px;
    display: flex; align-items: center; gap: 10px;
  }
  .brand-mark { width: 26px; height: 26px; border-radius: 50%; background: var(--navy); }
  .brand-name { font-size: 22px; font-weight: 600; color: var(--navy); letter-spacing: 0.5px; }

  .contact {
    position: absolute; left: 320px; top: 56px;
    display: flex; gap: 6px;
    font-size: 7.5px; line-height: 13px; color: var(--navy);
  }
  .contact-icons { display: flex; flex-direction: column; gap: 0; padding-top: 2px; }
  .contact-icons svg { width: 9px; height: 9px; margin-bottom: 4px; }
  .contact-icons svg:first-child { margin-bottom: 17px; }
  .contact-rule { width: 1px; background: var(--red); }

  .letter-body {
    position: absolute; left: 62px; top: 190px; width: 420px;
    font-size: 9px; line-height: 16px; color: var(--ink);
  }
  .letter-body p { margin-bottom: 14px; }
  .sign-off { position: absolute; left: 96px; top: 480px; font-size: 9px; line-height: 16px; color: var(--ink); }

  .seal {
    position: absolute; left: 420px; top: 548px;
    width: 110px; height: 110px; border-radius: 50%;
    background: var(--faint-navy); opacity: 0.6;
  }
  .seal-name {
    position: absolute; left: 420px; top: 664px; width: 110px; text-align: center;
    font-size: 10px; font-weight: 600; color: var(--faint-navy);
  }
</style>
</head>
<body>
  <main class="letterhead">
    <div class="band-top-navy"></div>
    <div class="band-top-red"></div>

    <div class="brand">
      <span class="brand-mark"></span>
      <span class="brand-name">Vantrell Law</span>
    </div>

    <div class="contact">
      <div class="contact-icons">
        <svg viewBox="0 0 10 10" aria-hidden="true"><path d="M5 0a3.5 3.5 0 0 0-3.5 3.5C1.5 6 5 10 5 10s3.5-4 3.5-6.5A3.5 3.5 0 0 0 5 0zm0 5a1.4 1.4 0 1 1 0-2.8A1.4 1.4 0 0 1 5 5z" fill="#e21d25"/></svg>
        <svg viewBox="0 0 10 10" aria-hidden="true"><path d="M2 1l2 2-1 1.2a6 6 0 0 0 2.8 2.8L7 6l2 2-1.2 1.5C4.5 9.5.5 5.5.5 2.2z" fill="#e21d25"/></svg>
        <svg viewBox="0 0 10 10" aria-hidden="true"><rect x="1" y="3" width="8" height="5" rx="1" fill="#e21d25"/><rect x="3" y="1" width="4" height="2.5" fill="#e21d25"/></svg>
      </div>
      <div class="contact-rule"></div>
      <div class="contact-lines">
        <div>4817 Larkspur Boulevard, Suite 250,</div>
        <div>Houston, Texas 77342</div>
        <div>832-619-3057</div>
        <div>832-407-1694</div>
      </div>
    </div>

    <section class="letter-body">
      <p>Dear Customer,</p>
      <p>Lorem ipsum dolor sit amet, consectetur adipiscing elit. Aenean ut ipsum eget massa hendrerit vestibulum vel in velit. Donec pretium neque velit.</p>
      <p>Aliquam porta lectus nec mauris ornare venenatis. Vivamus non est turpis, et cursus sem. Mauris vehicula erat in diam auctor at bibendum nisl lacinia.</p>
      <p>Morbi imperdiet neque vehicula nunc convallis gravida. Vestibulum iaculis pretium placerat. Integer consequat, est sit amet facilisis eleifend, nibh nibh varius orci, eget dapibus arcu dui non purus. Pellentesque in magna mauris. Duis enim sapien, dictum vitae condimentum a, pulvinar vel lacus. Mauris et molestie nibh. Vestibulum vitae nulla at metus elementum porta sit amet interdum elit. Nulla sollicitudin neque eu nulla volutpat congue.</p>
      <p>Etiam pellentesque, velit id dapibus fermentum, turpis sapien ornare dui, ac tincidunt ligula odio congue purus. Nunc sed ante dui, in porta lectus. Cras nec sem lorem. In hac habitasse platea dictumst. Maecenas id diam quis dui porta tristique. Sed id egestas felis. Donec ullamcorper mattis posuere. Phasellus fermentum eleifend tortor vel dapibus. Vestibulum ante ipsum.</p>
    </section>

    <div class="sign-off">Your Sincerely,<br>Managing Director</div>

    <div class="seal"></div>
    <div class="seal-name">Vantrell Law</div>

    <div class="band-bottom-red"></div>
    <div class="band-bottom-navy"></div>
  </main>
</body>
</html>
```